Financial Sevices firm looking for Brochure design

Our company Veltmoor Capital and Holdings Limited (VeltHoldings)
i
Is an investment/advisory firm - www.veltholdings-grp.net
We invest in the energy sector in Africa and offer advisory services to Energy companies looking to invest in Africa. From oil and gas, to renewables (wind/solar). We are more focused on the "West African" Sub region
We need corporate brochure (Booklet style) to circulate to our corporate clients
We would like to see a design that considers the colours in our Logo (see website)
HI Guys, sorry been travelling. Seen some very good submissions and will be sending updates shortly
Reason: Dear Designers,
Thank you for participating in this project and for some of the great designs i've received so far. Unfortunately, due to the holidays, it has been difficult to consult with other members of my team. As a result, the project deadline is extended by about 12 days
I appreciate your understanding in the situation and looking forward to continuing the excellent collaboration in the coming days
Reason: Hi All,
Apologies for the multiple deadline extensions and thanks so much for all the designs which my team and I will be reviewing today and tomorrow.
We will be closing this project tomorrow by 6pm GMT (17th Jan 2014)
Thanks to all those that submitted such wonderful designs and goodluck!!
Project to be closed finally on 17th Jan 2014 at 6pm GMT
Banks, Investment Firms, Energy companies, Private Equity Funds
I have attached a Brochure that I created myself as an example of the type of information required but please also feel free to visit our website www.veltholdings-grp.net
Looking for any creative ideas you have to suplement the information provided.
Financial

```html
<!DOCTYPE html>
<html lang="en">
<head>
<meta charset="utf-8">
<title>Veltmoor Capital and Holdings Limited — Brochure Spread</title>
<link href="https://fonts.googleapis.com/css2?family=Montserrat:wght@400;500;600;700&display=swap" rel="stylesheet">
<style>
  :root {
    --bg: #eeeeee;
    --page: #ffffff;
    --brand-red: #cd1426;
    --slate: #5b5e62;
    --ink: #4a4a4c;
    --photo-light: #c9ccd0;
    --photo-dark: #5c6066;
    --caption-bg: rgba(20, 20, 20, 0.82);
  }
  * { box-sizing: border-box; margin: 0; padding: 0; }
  html, body {
    width: 1200px; height: 849px; overflow: hidden;
    background: var(--bg);
    font-family: "Montserrat", Arial, sans-serif;
  }
  .spread { position: absolute; left: 114px; top: 181px; width: 964px; height: 481px; }

  /* Left page */
  .page-left { position: absolute; left: 0; top: 0; width: 482px; height: 481px; background: var(--page); }
  .intro-band {
    position: absolute; left: 0; top: 0; width: 482px; height: 159px;
    background: var(--brand-red); color: #fff;
    padding: 44px 36px 0 33px;
    font-size: 12.3px; line-height: 16.3px; text-align: justify;
  }
  .expertise-band {
    position: absolute; left: 0; top: 161px; width: 482px; height: 158px;
    background: var(--slate); color: #fff;
    padding: 38px 36px 0 33px;
    font-size: 16.6px; line-height: 20.2px; text-align: justify; font-weight: 400;
  }
  .photo-band {
    position: absolute; left: 0; top: 322px; width: 482px; height: 159px;
    background: linear-gradient(160deg, var(--photo-light) 0%, #9a9ea4 45%, var(--photo-dark) 100%);
  }
  .tagline {
    position: absolute; left: 92px; top: 54px; width: 300px; height: 50px;
    background: var(--caption-bg); text-align: center; color: #fff;
    padding-top: 5px;
  }
  .tagline-lead { font-size: 12px; line-height: 15px; }
  .tagline-words { font-size: 18.5px; line-height: 24px; color: var(--brand-red); font-weight: 500; }
  .tagline-words .mark { color: #fff; }

  /* Right page */
  .page-right { position: absolute; left: 482px; top: 0; width: 482px; height: 481px; background: var(--page); }
  .brand-name {
    position: absolute; right: 14px; top: 13px;
    display: flex; align-items: center; gap: 4px;
    font-size: 9px; font-weight: 600; color: var(--brand-red);
  }
  .brand-name .square { width: 8px; height: 8px; background: var(--brand-red); }
  .quote-open, .quote-close {
    position: absolute; color: var(--brand-red); font-size: 40px; font-weight: 700; line-height: 1;
    font-family: Georgia, "Times New Roman", serif;
  }
  .quote-open { left: 34px; top: 44px; }
  .quote-close { left: 402px; top: 118px; }
  .statement {
    position: absolute; left: 36px; top: 70px; width: 416px;
    font-size: 11.3px; line-height: 16.5px; color: var(--ink);
    text-transform: uppercase; text-align: justify; letter-spacing: 0.1px;
  }
  .pillar { position: absolute; left: 36px; width: 416px; }
  .pillar-title {
    display: flex; align-items: center; gap: 5px;
    color: var(--brand-red); font-weight: 600; font-size: 12.3px; text-transform: uppercase;
  }
  .pillar-title svg { width: 24px; height: 20px; }
  .pillar-text { margin-top: 5px; font-size: 7.6px; line-height: 10.6px; color: var(--ink); text-align: justify; }
  .vision { top: 170px; }
  .mission { top: 287px; }
  .values { top: 370px; }
  .values-list { margin-top: 6px; font-size: 14.8px; font-weight: 600; color: var(--slate); letter-spacing: 0.2px; }
</style>
</head>
<body>
<main class="spread">
  <section class="page-left">
    <div class="intro-band">
      We are dedicated to promoting the sustainable implementation of infrastructure and energy related projects in Africa through direct investments and by facilitating private and institutional investments. Our narrow sector focus enables us to provide in-depth services and insightful investment solutions.
    </div>
    <div class="expertise-band">
      Our team brings a wealth of international expertise in the areas of transaction structuring, public-private partnerships (PPP), financial and economic modeling, legal and regulatory reform, and operations.
    </div>
    <div class="photo-band" role="img" aria-label="Black and white photograph of a building under construction with a crane against a cloudy sky">
      <div class="tagline">
        <p class="tagline-lead">Our Triple Bottom Line is:</p>
        <p class="tagline-words"><span class="mark">“</span>PEOPLE, PROFIT &amp; PLANET<span class="mark">”</span></p>
      </div>
    </div>
  </section>

  <section class="page-right">
    <div class="brand-name"><span class="square"></span>VeltHoldings</div>
    <span class="quote-open">“</span>
    <p class="statement">Veltmoor Capital and Holdings Limited is an independent, integrated investment and consulting company with extensive experience in structuring and developing projects in Africa.</p>
    <span class="quote-close">”</span>

    <div class="pillar vision">
      <h2 class="pillar-title">
        <svg viewBox="0 0 24 20" aria-hidden="true"><ellipse cx="12" cy="10" rx="11" ry="7" fill="var(--brand-red)"/><circle cx="12" cy="10" r="4.2" fill="#fff"/><circle cx="12" cy="10" r="2.2" fill="var(--brand-red)"/></svg>
        Our Vision
      </h2>
      <p class="pillar-text">To contribute to the implementation of robust infrastructure towards enhanced socio-economic development in Africa.<br>We are dedicated to promoting the implementation of infrastructure and energy related projects in Africa through direct investment or by the facilitation of other’s investments. Our narrow sector focus enables us to provide in-depth services and insightful investment solutions.</p>
    </div>

    <div class="pillar mission">
      <h2 class="pillar-title">
        <svg viewBox="0 0 24 20" aria-hidden="true"><circle cx="11" cy="10" r="8.5" fill="none" stroke="var(--brand-red)" stroke-width="1.8"/><path d="M15 6 L12.2 11.2 L7 14 L9.8 8.8 Z" fill="var(--brand-red)"/></svg>
        Our Mission
      </h2>
      <p class="pillar-text">To create the greatest value for our clients and investors through the efficient implementation of infrastructure and energy related projects across Africa.</p>
    </div>

    <div class="pillar values">
      <h2 class="pillar-title">
        <svg viewBox="0 0 24 20" aria-hidden="true"><g transform="translate(11 10)" fill="var(--brand-red)"><circle r="6.5"/><rect x="-1.8" y="-9.5" width="3.6" height="19"/><rect x="-1.8" y="-9.5" width="3.6" height="19" transform="rotate(45)"/><rect x="-1.8" y="-9.5" width="3.6" height="19" transform="rotate(90)"/><rect x="-1.8" y="-9.5" width="3.6" height="19" transform="rotate(135)"/><circle r="2.8" fill="#fff"/></g></svg>
        Our Values
      </h2>
      <p class="values-list">INTEGRITY, ACCOUNTABILITY, RESPECT, TEAM WORK</p>
    </div>
  </section>
</main>
</body>
</html>
```